External Window Signage Design – Antiaging Center

I would like to dress our shop windows in order to promote our activities in medical aesthetics, meso-aesthetics, anti-ageing care and classical beauty. In fact, our 350 m² center is located on the first floor of a building where there is a lot of traffic, as well as a bus stop and metro station. And right in front of a twenty-floor building of the Northern Tariff Bureau.
We want to communicate our activities to our customers with photos and text in a storefront window. So that they can what we do and visit our website www.lumivora.be (our site is in French) as well as our social networks, like picturegram, chatterbook,…
We'd like a window signage : Elegant, Modern, New, Pure, Clean
We are located on the corners of a building, where we have 8 windows on one side and 10 windows on the other, the dimensions are :
Windows
• Height: 125 cm
• Width: 130 cm
Small windows
• Height: 134 cm
• Width: 40 cm
I would say let your imagination go free. I will have other projects for the winner.
Don't hesitate to ask me if you need other formats of the logo or color, like white.
Updates

https://www.pixelbazaar-example.com/design/58204917, I'D LIKE TO HAVE A PROJECT LIKE THIS IF POSSIBLE WITH THE LITTLE WINDOW UNDERNEATH AS WELL.

Target Market(s)

People who want to take care of their external appearance, look beautiful and good looking, womens/girls - mens/boys

Requirements
Must have
• Face and silhouette of a woman. Elegant
Serious, Modern, Professional, Feminine,Upmarket
Nice to have
• To put the different treatments that we propose,
Should not have
• We absolutely don't want a classic beauty center signage, which is reviewed many times

```html
<!DOCTYPE html>
<html lang="en">
<head>
<meta charset="utf-8">
<title>Lumivora – Window Signage</title>
<link rel="stylesheet" href="https://fonts.googleapis.com/css2?family=Open+Sans:wght@400&family=Roboto:wght@300;400;700&display=swap">
<style>
  :root{
    --bg-light:#ececec;
    --bg-dark:#b9b9b9;
    --panel-grey:#e6e6e6;
    --white:#ffffff;
    --gold:#b59a5a;
    --red:#c8102e;
    --ink:#222222;
    --logo-ink:#333333;
    --sub-ink:#555555;
    --rule:#555555;
    --skin-1:#f3d9c8;
    --skin-2:#e8b89b;
  }
  *{margin:0;padding:0;box-sizing:border-box}
  html,body{width:1200px;height:1200px;overflow:hidden}
  body{
    position:relative;
    background:radial-gradient(ellipse at 50% 45%, var(--bg-light) 0%, #dcdcdc 50%, var(--bg-dark) 100%);
    font-family:"Roboto",Arial,sans-serif;
    color:var(--ink);
  }
  .panel{position:absolute;background:var(--white);overflow:hidden}
  .panel > svg.backdrop{position:absolute;left:0;top:0;width:100%;height:100%}
  .abs{position:absolute}

  .banner{left:68px;top:221px;width:226px;height:759px}
  .window{left:342px;top:224px;width:783px;height:752px}

  .brand-mark{position:absolute;border-radius:50%;background:var(--gold)}
  .brand-name{position:absolute;font-family:"Roboto",Arial,sans-serif;font-weight:700;color:var(--logo-ink);white-space:nowrap;line-height:1;letter-spacing:-0.02em}
  .brand-tagline{position:absolute;font-family:"Open Sans",Arial,sans-serif;color:var(--sub-ink);white-space:nowrap;line-height:1}

  .title{position:absolute;color:var(--red);font-weight:300;line-height:1;white-space:nowrap;transform:translateX(-50%);letter-spacing:-0.02em}
  .rule{position:absolute;height:1px;background:var(--rule)}
  .rule-accent{position:absolute;background:var(--red)}
  .subtitle{position:absolute;color:var(--gold);font-weight:300;line-height:1;white-space:nowrap;transform:translateX(-50%);letter-spacing:-0.01em}
  .body-copy{position:absolute;text-align:justify;font-weight:400;color:var(--ink)}
  .body-copy .accent{color:var(--red)}

  .fact{position:absolute;text-align:center}
  .fact svg{display:block}
  .fact-label{display:block;color:#444;line-height:1.05;white-space:nowrap}

  .site{position:absolute;white-space:nowrap;line-height:1}
  .social{position:absolute;border-radius:50%}

  .size-label{position:absolute;top:992px;font-size:30px;font-weight:400;color:#222;white-space:nowrap;transform:translateX(-50%)}
</style>
</head>
<body>

<svg width="0" height="0" style="position:absolute">
  <defs>
    <symbol id="fact-frame" viewBox="0 0 60 64">
      <path d="M1 10V1h10" fill="none" stroke="#c8102e" stroke-width="1.2"/>
      <path d="M59 52v10h-10" fill="none" stroke="#c8102e" stroke-width="1.2"/>
      <rect x="5" y="4" width="50" height="54" fill="#fff" stroke="#444" stroke-width="1"/>
    </symbol>
    <symbol id="icon-steps" viewBox="0 0 60 64">
      <use href="#fact-frame"/>
      <text x="13" y="21" font-family="Roboto,Arial,sans-serif" font-weight="700" font-size="11" fill="#c8102e">1</text>
      <text x="13" y="33" font-family="Roboto,Arial,sans-serif" font-weight="700" font-size="11" fill="#c8102e">2</text>
      <text x="13" y="45" font-family="Roboto,Arial,sans-serif" font-weight="700" font-size="11" fill="#c8102e">3</text>
      <rect x="22" y="14" width="24" height="4" fill="#c8102e"/>
      <rect x="22" y="26" width="24" height="4" fill="#c8102e"/>
      <rect x="22" y="38" width="24" height="4" fill="#c8102e"/>
    </symbol>
    <symbol id="icon-timer" viewBox="0 0 60 64">
      <use href="#fact-frame"/>
      <circle cx="33" cy="33" r="12" fill="none" stroke="#c8102e" stroke-width="1.6"/>
      <rect x="30" y="16" width="6" height="3" fill="#c8102e"/>
      <path d="M33 33l5-6" stroke="#c8102e" stroke-width="1.6"/>
      <path d="M13 29h8M11 33h8M13 37h8" stroke="#c8102e" stroke-width="1.2"/>
    </symbol>
    <symbol id="icon-tag" viewBox="0 0 60 64">
      <use href="#fact-frame"/>
      <path d="M16 34l15-15h13v13L29 47z" fill="#c8102e"/>
      <circle cx="39" cy="24" r="2.2" fill="#fff"/>
    </symbol>
    <symbol id="icon-renew" viewBox="0 0 60 64">
      <use href="#fact-frame"/>
      <path d="M20 27a13 13 0 1 1 1 12" fill="none" stroke="#c8102e" stroke-width="2"/>
      <path d="M16 22l4 7 6-4" fill="none" stroke="#c8102e" stroke-width="2"/>
    </symbol>
    <linearGradient id="photo-tone" x1="0" y1="0" x2="1" y2="1">
      <stop offset="0" stop-color="#f2ece8"/>
      <stop offset="0.45" stop-color="#f0d3c2"/>
      <stop offset="1" stop-color="#e3b398"/>
    </linearGradient>
  </defs>
</svg>

<!-- Narrow window banner -->
<section class="panel banner">
  <svg class="backdrop" viewBox="0 0 226 759" preserveAspectRatio="none">
    <polygon points="0,89 226,89 226,294 66,453 0,392" fill="url(#photo-tone)" role="img" aria-label="Photo of a woman with closed eyes, hands framing her face"/>
    <polygon points="226,294 131,388 226,478" fill="var(--gold)"/>
    <polygon points="0,403 29,431 0,456" fill="var(--red)"/>
    <rect x="0" y="737" width="226" height="22" fill="var(--gold)"/>
  </svg>

  <div class="brand-mark" style="left:25px;top:30px;width:32px;height:32px"></div>
  <div class="brand-name" style="left:66px;top:33px;font-size:27px">Lumivora</div>
  <div class="brand-tagline" style="left:94px;top:60px;font-size:11.5px">Antiaging Center</div>

  <div class="title" style="left:113px;top:489px;font-size:33px">ANTIAGING</div>
  <div class="rule" style="left:37px;top:522px;width:153px"></div>
  <div class="rule-accent" style="left:100px;top:520px;width:27px;height:4px"></div>
  <div class="subtitle" style="left:113px;top:531px;font-size:22px">Wrinkle Filling</div>

  <p class="body-copy" style="left:24px;top:567px;width:178px;font-size:8.4px;line-height:11.5px">
    We offer mechanical treatments that stimulate your dermis, but also chemical treatments that awaken the hyaluronic acid and collagen present in your skin to give <span class="accent">your face, neck and chest a youthful look .</span>
  </p>

  <div class="fact" style="left:23px;top:656px;width:36px">
    <svg width="36" height="38"><use href="#icon-steps"/></svg>
    <span class="fact-label" style="font-size:5.5px">1 session</span>
  </div>
  <div class="fact" style="left:70px;top:656px;width:36px">
    <svg width="36" height="38"><use href="#icon-timer"/></svg>
    <span class="fact-label" style="font-size:5.5px">+/- 45minutes</span>
  </div>
  <div class="fact" style="left:116px;top:656px;width:36px">
    <svg width="36" height="38"><use href="#icon-tag"/></svg>
    <span class="fact-label" style="font-size:5.5px">From 180 €</span>
  </div>
  <div class="fact" style="left:163px;top:656px;width:36px">
    <svg width="36" height="38"><use href="#icon-renew"/></svg>
    <span class="fact-label" style="font-size:5.5px">9 to 12<br>months</span>
  </div>

  <div class="site" style="left:47px;top:741px;font-size:13px;color:var(--white);font-weight:300">www.lumivora.be</div>
  <div class="social" style="left:159px;top:743px;width:10px;height:10px;background:var(--white)"></div>
  <div class="social" style="left:176px;top:743px;width:10px;height:10px;background:var(--white)"></div>
</section>

<!-- Large window panel -->
<section class="panel window">
  <svg class="backdrop" viewBox="0 0 783 752" preserveAspectRatio="none">
    <polygon points="0,0 783,0 783,117 211,705 0,494" fill="var(--panel-grey)"/>
    <polygon points="0,50 419,50 419,497 211,705 0,494" fill="url(#photo-tone)" role="img" aria-label="Photo of a woman with closed eyes, hands framing her face"/>
    <polygon points="783,131 609,304 783,463" fill="var(--gold)"/>
    <polygon points="0,522 73,587 0,661" fill="var(--red)"/>
  </svg>

  <div class="brand-mark" style="left:336px;top:62px;width:88px;height:88px"></div>
  <div class="brand-name" style="left:440px;top:56px;font-size:66px">Lumivora</div>
  <div class="brand-tagline" style="left:494px;top:125px;font-size:25px">Antiaging Center</div>

  <div class="title" style="left:601px;top:430px;font-size:55px">ANTIAGING</div>
  <div class="rule" style="left:478px;top:496px;width:244px"></div>
  <div class="rule-accent" style="left:577px;top:493px;width:45px;height:7px"></div>
  <div class="subtitle" style="left:601px;top:505px;font-size:37px">Wrinkle Filling</div>

  <p class="body-copy" style="left:438px;top:557px;width:323px;font-size:14px;line-height:17.5px">
    We offer mechanical treatments that stimulate your dermis, but also chemical treatments that awaken the hyaluronic acid and collagen present in your skin to give <span class="accent">your face, neck and chest a youthful look .</span>
  </p>

  <div class="fact" style="left:451px;top:651px;width:60px">
    <svg width="60" height="64"><use href="#icon-steps"/></svg>
    <span class="fact-label" style="font-size:9.5px;margin-top:2px">1 session</span>
  </div>
  <div class="fact" style="left:528px;top:651px;width:60px">
    <svg width="60" height="64"><use href="#icon-timer"/></svg>
    <span class="fact-label" style="font-size:9.5px;margin-top:2px">+/- 45minutes</span>
  </div>
  <div class="fact" style="left:604px;top:651px;width:60px">
    <svg width="60" height="64"><use href="#icon-tag"/></svg>
    <span class="fact-label" style="font-size:9.5px;margin-top:2px">From 180 €</span>
  </div>
  <div class="fact" style="left:681px;top:651px;width:60px">
    <svg width="60" height="64"><use href="#icon-renew"/></svg>
    <span class="fact-label" style="font-size:9.5px;margin-top:2px">9 to 12<br>months</span>
  </div>

  <div class="site" style="left:20px;top:675px;font-size:20px;color:var(--red);font-weight:400">www.lumivora.be</div>
  <div class="social" style="left:65px;top:701px;width:22px;height:22px;background:#2b2b2b"></div>
  <div class="social" style="left:98px;top:701px;width:22px;height:22px;background:#2b2b2b"></div>
</section>

<div class="size-label" style="left:181px">134 cm x 40 cm</div>
<div class="size-label" style="left:733px">125 cm x 130 cm</div>

</body>
</html>
```